serious, thorough, light and simple - that's my advice and mediations

My business card should combine my logo (uploaded file) and my homepage (https://feltra-mediation.plavosite.com).

Contact Information for Business Card

Name: Sabine Feltra di Olvesi
Phone: 079 417 68 92
mail: sfeltra@plovix.ch
web: www.feltra-di-olvesi.ch

```html
<!DOCTYPE html>
<html lang="de">
<head>
<meta charset="utf-8">
<title>Visitenkarte – Sabine Feltra di Olvesi</title>
<link href="https://fonts.googleapis.com/css2?family=Montserrat:wght@400;500&display=swap" rel="stylesheet">
<style>
  :root {
    --backdrop: #d0d0d0;
    --card: #ffffff;
    --ink-blue: #2e3a87;
    --accent-green: #17795a;
    --icon-teal: #2a6f86;
  }
  * { margin: 0; padding: 0; box-sizing: border-box; }
  html, body {
    width: 1200px; height: 933px; overflow: hidden;
    background: var(--backdrop);
    font-family: "Montserrat", Arial, sans-serif;
  }
  .card {
    position: absolute; left: 321px; width: 558px; height: 320px;
    background: var(--card);
  }
  .card--front { top: 87px; }
  .card--back { top: 467px; }

  .brand {
    position: absolute; inset: 0;
    display: flex; align-items: center; justify-content: center;
    margin-top: -6px;
  }
  .brand__name {
    font-size: 32px; font-weight: 500; color: var(--ink-blue);
    letter-spacing: 0.5px; line-height: 1;
  }

  .holder {
    position: absolute; left: 51px; top: 154px;
    font-size: 18.5px; font-weight: 500; color: var(--ink-blue);
    line-height: 1;
  }
  .divider {
    position: absolute; left: 286px; top: 95px; width: 1.5px; height: 147px;
    background: linear-gradient(var(--ink-blue), var(--accent-green));
  }
  .contacts {
    position: absolute; left: 316px; top: 125px; list-style: none;
  }
  .contacts__item {
    display: flex; align-items: center; height: 31px;
    font-size: 14px; color: var(--ink-blue);
  }
  .contacts__icon { width: 13px; height: 13px; margin-right: 11px; flex: none; }
</style>
</head>
<body>
  <section class="card card--front">
    <div class="brand">
      <span class="brand__name">Klarweg Mediation</span>
    </div>
  </section>

  <section class="card card--back">
    <p class="holder">Sabine Feltra di Olvesi</p>
    <span class="divider"></span>
    <ul class="contacts">
      <li class="contacts__item">
        <svg class="contacts__icon" viewBox="0 0 13 13" fill="none" stroke="var(--icon-teal)" stroke-width="1.2">
          <rect x="3.5" y="0.8" width="6" height="11.4" rx="1"/>
          <line x1="5.8" y1="10.3" x2="7.2" y2="10.3"/>
        </svg>079 417 68 92
      </li>
      <li class="contacts__item">
        <svg class="contacts__icon" viewBox="0 0 13 13" fill="none" stroke="var(--icon-teal)" stroke-width="1.2">
          <rect x="0.8" y="2.5" width="11.4" height="8" rx="1"/>
          <polyline points="1,3 6.5,7 12,3"/>
        </svg>sfeltra@plovix.ch
      </li>
      <li class="contacts__item">
        <svg class="contacts__icon" viewBox="0 0 13 13" fill="none" stroke="var(--icon-teal)" stroke-width="0.9">
          <circle cx="6.5" cy="6.5" r="5.7"/>
          <ellipse cx="6.5" cy="6.5" rx="2.6" ry="5.7"/>
          <line x1="0.8" y1="6.5" x2="12.2" y2="6.5"/>
          <line x1="1.6" y1="3.8" x2="11.4" y2="3.8"/>
          <line x1="1.6" y1="9.2" x2="11.4" y2="9.2"/>
        </svg>www.feltra-di-olvesi.ch
      </li>
    </ul>
  </section>
</body>
</html>
```